Industry: Christian Ministry using Magic, Music and Multimedia to teach gospel

“Lanternfold Ministries brings the Gospel of Jesus Christ, with heart-seeking, biblical accuracy
through live, entertainment-based evangelistic Celebrations."

We are a service that wants to partner with christian religious institutions and churches to teach biblical gospel in a fun and entertaining way using magic.

Design inspiration: https://www.quillmarshwonders.example

DO NOT CONTACT ME PRIVATELY. IT WILL BE IGNORED.

Important:
1. Use only royalty free graphics
2. Use only google fonts
3. A clean, linear layout
4. Do not include search

PAGES

1. Home
2. Shows & Skylark
3. About Lanternfold
4. Media
5. Contact & Support

Color pallets
#0053E0
#FF2500
#ffffff

Please see attachment for more detail

Target Market(s)

Churches and christian schools

Industry/Entity Type

magic, entertainment, christianity

Number of Pages Required

5+ page

Colors
0054AA
0677BA
7BADD7
CADEEF
E8F1F8

Requirements
Should not have
• - search bar

```html
<!DOCTYPE html>
<html lang="en">
<head>
<meta charset="utf-8">
<title>About Lanternfold</title>
<link href="https://fonts.googleapis.com/css2?family=Poppins:wght@400;500;600;700&display=swap" rel="stylesheet">
<style>
:root{
  --nav:#0a4fc4;
  --hero-deep:#0a3d9a;
  --hero-mid:#0b63c9;
  --hero-glow:#29a8f0;
  --band-deep:#0b72c8;
  --band-light:#5fc3f0;
  --ink:#1f2433;
  --ink-soft:#2d3345;
  --white:#ffffff;
  --button:#5aa9dc;
  --footer:#0a4fbf;
}
*{box-sizing:border-box;margin:0;padding:0}
html,body{width:1200px;height:5020px;overflow:hidden}
body{font-family:"Poppins",sans-serif;color:var(--ink);background:var(--white);position:relative}
.site-nav{position:absolute;top:0;left:0;width:1200px;height:94px;background:var(--nav);display:flex;justify-content:center;align-items:center;gap:39px;padding-right:30px}
.site-nav a{color:var(--white);text-decoration:none;font-size:24px;font-weight:500}
.hero{position:absolute;top:94px;left:0;width:1200px;height:656px;background:radial-gradient(ellipse 55% 70% at 45% 25%,var(--hero-glow) 0%,var(--hero-mid) 45%,var(--hero-deep) 100%);overflow:hidden}
.hero-wave{position:absolute;left:0;top:0}
.hero-eyebrow{position:absolute;left:105px;top:100px;color:var(--white);font-size:18px;font-weight:600}
.hero-title{position:absolute;left:102px;top:118px;color:var(--white);font-size:56px;font-weight:600;line-height:68px}
.hero-text{position:absolute;left:103px;top:276px;width:520px;color:var(--white);font-size:20.5px;line-height:25px}
.hero-button{position:absolute;left:103px;top:455px;width:152px;height:55px;background:var(--button);color:var(--white);font-size:16px;font-weight:600;border-radius:4px;display:flex;align-items:center;justify-content:center}
.hero-image{position:absolute;left:748px;top:81px;width:356px;height:355px;background:radial-gradient(circle at 50% 28%,#f4d9a0 0%,#8a6a4a 18%,#2a2430 45%,#141620 100%)}
.programs{position:absolute;top:800px;left:0;width:1200px;text-align:center}
.section-title{font-size:41px;font-weight:500;color:var(--ink)}
.programs .section-title{margin-top:16px}
.body-text{font-size:23px;line-height:29.5px;color:var(--ink-soft)}
.programs .lead{margin:40px auto 0;width:1000px}
.program-list{position:absolute;top:270px;left:0;width:1200px}
.program-list ul{position:absolute;list-style:disc;text-align:left;font-size:24px;line-height:32px;padding-left:30px}
.programs .closing{position:absolute;top:424px;left:110px;width:980px}
.rays{position:absolute;top:1410px;left:0;width:1200px;height:846px;background:radial-gradient(ellipse 70% 60% at 50% 40%,var(--band-light) 0%,#2c9ee0 45%,var(--band-deep) 100%);color:var(--white);text-align:center}
.rays-title{position:absolute;top:100px;left:0;width:1200px;font-size:62px;font-weight:700;line-height:74px}
.rays p{position:absolute;left:110px;width:980px;font-size:23px;line-height:29.5px}
.difference{position:absolute;top:2320px;left:0;width:1200px;height:800px}
.diff-title{position:absolute;left:105px;top:0;font-size:39px;font-weight:600;line-height:50px;text-transform:uppercase;color:var(--ink)}
.diff-text{position:absolute;left:107px;top:246px;width:650px}
.diff-image{position:absolute;left:803px;top:183px;width:296px;height:283px;background:radial-gradient(circle at 45% 40%,#e23b2c 0%,#c81e14 25%,#f1f1f1 55%,#ffffff 100%)}
.diff-more{position:absolute;left:105px;top:528px;width:1000px}
.faith{position:absolute;top:3156px;left:0;width:1200px;height:847px;background:radial-gradient(ellipse 70% 60% at 50% 45%,var(--band-light) 0%,#2c9ee0 45%,var(--band-deep) 100%);color:var(--white);text-align:center}
.faith-title{padding-top:52px;font-size:62px;font-weight:700;line-height:76px}
.faith-list{width:940px;margin:14px auto 0;font-size:23px;line-height:29.5px}
.faith-list p{margin-bottom:29px}
.faith-list strong{font-weight:700}
.faq{position:absolute;top:4040px;left:0;width:1200px}
.faq-title{position:absolute;left:101px;top:0;font-size:64px;font-weight:700;color:#000}
.faq h3{position:absolute;left:101px;font-size:30px;font-weight:600;text-transform:uppercase;color:var(--ink)}
.faq p{position:absolute;left:101px;width:1000px}
.site-footer{position:absolute;top:4767px;left:0;width:1200px;height:253px;background:var(--footer);color:var(--white)}
.footer-heading{position:absolute;top:58px;font-size:21px;font-weight:500}
.footer-pages{position:absolute;left:123px;top:93px;list-style:none;font-size:13px;line-height:21.5px}
.footer-field{position:absolute;height:29px;background:var(--white);color:#333;font-size:9px;padding:9px 8px;text-transform:uppercase}
.footer-submit{position:absolute;left:916px;top:200px;width:101px;height:20px;background:var(--white);color:#222;border-radius:10px;font-size:10px;font-weight:600;display:flex;align-items:center;justify-content:center}
</style>
</head>
<body>
<nav class="site-nav">
  <a href="#">Home</a>
  <a href="#">Shows &amp; Skylark</a>
  <a href="#">About Lanternfold</a>
  <a href="#">Media</a>
  <a href="#" style="margin-left:8px">Contact &amp; Support</a>
</nav>

<header class="hero">
  <div class="hero-eyebrow">ABOUT LANTERNFOLD</div>
  <h1 class="hero-title">About Magical<br>Christian Entertainer</h1>
  <p class="hero-text">Christian magician we can has teamed with churches, camps, conferences, and other Christian groups all around the nation and the world to bring people in for fun, humor, and inspiration.</p>
  <div class="hero-button">Contact Us</div>
  <div class="hero-image" role="img" aria-label="Glowing light bulb hanging above an open book with drifting smoke"></div>
  <svg class="hero-wave" width="1200" height="656" viewBox="0 0 1200 656" aria-hidden="true">
    <path d="M0 598 C80 630 150 660 260 652 C420 640 560 560 760 550 C900 543 1040 560 1200 610 L1200 656 L0 656 Z" fill="#ffffff"/>
  </svg>
</header>

<section class="programs">
  <h2 class="section-title">Types of Christian Magic Programs</h2>
  <p class="body-text lead">We have created innumerable routines over the years for a wide range of circumstances. We are prepared to create a Christian magic program specifically for you. We frequently collaborate with a variety of Christian groups, both big and small, like:</p>
  <div class="program-list">
    <ul style="left:106px"><li>churches</li><li>schools</li><li>camps</li></ul>
    <ul style="left:479px"><li>conferences</li><li>retreats</li><li>banquets</li></ul>
    <ul style="left:890px"><li>fellowships</li><li>fundraisers</li><li>and more...</li></ul>
  </div>
  <p class="body-text closing">Therefore, whether you're seeking for evangelism, inspiration, education, or just pure entertainment, we are prepared to tailor a program to match your specific goals.For reservations or to discuss what we can accomplish together, get in touch with us.</p>
</section>

<section class="rays">
  <h2 class="rays-title">So what exactly is a<br>Christian magician?</h2>
  <p style="top:322px">Glad you inquired! According to one definition, theatrical magic is "the art of using natural causes, whose operation is secret, to produce surprising results. " Consequently, a magician is an entertainer that engages audiences and inspires awe by utilizing science, chemistry, psychology, deception, and other techniques.</p>
  <p style="top:579px">A "Christian magician" only employs this sort of art as a means of proclamation. But how this seems can vary greatly from one episode to the next. This could entail delivering the Gospel, exemplifying a biblical message, or simply offering clean, family-friendly enjoyment, depending on the requirements of the occasion.</p>
</section>

<section class="difference">
  <h2 class="diff-title">What’s the difference between a<br>Christian magician and a Christian<br>illusionist?</h2>
  <p class="body-text diff-text">The term "illusionist" in magic or illusion refers to a performer who employs their skills to portray grand effects, typically involving people or large animals. However, the terms magician and illusionist are frequently used interchangeably in everyday speech.</p>
  <div class="diff-image" role="img" aria-label="White figure leaning against a large red question mark"></div>
  <p class="body-text diff-more">Technically speaking, Christian magician is a better term to describe the majority of what we do, even though some of our routines could be categorized as illusions. The capacity to entertain and engage audiences, no matter how big or little, while spreading the gospel is what matters. Therefore, whether you refer to him as a "Christian Magician" or a "Christian Illusionist" before the event, your group will probably describe him as spectacular, enjoyable, and humorous in the end.</p>
</section>

<section class="faith">
  <h2 class="faith-title">Statement of Faith</h2>
  <div class="faith-list">
    <p><strong>I believe</strong> the Bible is the inspired, authoritative Word of God, inerrant in its original manuscripts.</p>
    <p><strong>I believe</strong> there is one God, eternally existent in three persons: Father, Son, and Holy Spirit.</p>
    <p><strong>I believe</strong> in the deity of the Lord Jesus Christ, His virgin birth, His sinless life, His miracles, His vicarious and atoning death, His bodily resurrection, His ascension to the right hand of the Father, and His personal return in power and glory.</p>
    <p><strong>I believe</strong> that sinful man can only come to God through faith in Jesus Christ.</p>
    <p><strong>I believe</strong> in the present ministry of the Holy Spirit by whose indwelling the Christian is enabled to live a godly life.</p>
    <p><strong>I believe</strong> in the resurrection of both the saved and the lost, they that are saved unto the resurrection of life, and they that are lost to the resurrection of damnation.</p>
    <p><strong>I believe</strong> in the spiritual unity of believers in our Lord Jesus Christ.</p>
  </div>
</section>

<section class="faq">
  <h2 class="faq-title">Frequently Asked Question</h2>
  <h3 style="top:140px">How did you do that?</h3>
  <p class="body-text" style="top:214px">Magicians don’t generally share their secrets, but we’ll make an exception<br>in this case.</p>
  <p class="body-text" style="top:302px">My feats are accomplished through psychology, misdirection, physics, chemistry, and a whole lot of practice.</p>
  <h3 style="top:382px">Are you a magician, or an illusionist?</h3>
  <p class="body-text" style="top:456px">All magicians are illusionists, but not all illusionists are magicians. The term "magician" is used broadly to describe those who perform illusions, mentalism, close-up magic, and other types of magic. A person who performs elaborate stage effects with humans, animals, or very large items is known as an illusionist. I practice a wide range of magic. Even if some of the things I perform could be categorized as illusions, some wouldn't. Therefore, "magician" is the most accurate general term.<br>(whatever, feel free to address me whatever you like!)</p>
</section>

<footer class="site-footer">
  <div class="footer-heading" style="left:123px">Pages</div>
  <ul class="footer-pages">
    <li>Home</li><li>Shows &amp; Skylark</li><li>About Lanternfold</li><li>Media</li><li>Contact &amp; Support</li>
  </ul>
  <div class="footer-heading" style="left:633px">Contact us</div>
  <div class="footer-field" style="left:633px;top:93px;width:181px">First name</div>
  <div class="footer-field" style="left:836px;top:93px;width:181px">Last name</div>
  <div class="footer-field" style="left:633px;top:148px;width:384px">Email address</div>
  <div class="footer-submit">SUBMIT</div>
</footer>
</body>
</html>
```